Brindle Logistics Business Card Design

We are a trucking and warehousing company. We run freight in the US manly from the Pacific NW to TX and back up the the PNW. We also do warehousing where we store, move, and distribute freight. Looking for a clean and modern design of business card. We would like to look rich and elegant. Attached is our logo.

Industry/Entity Type

Trucking Company

Contact Information for Business Card

Looking for a clean and modern design of business card. We would like to look rich and elegant.

Font styles to use
Sans Serif

Colors

Designer to choose colors to be used in the design.

Requirements
Must have
• logo but it should not dominate the card
Should not have
• logo should not dominate the card

```html
<!DOCTYPE html>
<html lang="en">
<head>
<meta charset="utf-8">
<title>Brindle Logistics Business Card</title>
<link rel="stylesheet" href="https://fonts.googleapis.com/css2?family=Open+Sans:wght@400;600;700&family=Roboto+Slab:wght@600&display=swap">
<style>
  :root {
    --page: #e6e4e1;
    --card: #2a2a2c;
    --card-edge: #1f1f21;
    --ink: #f2f2f2;
    --ink-soft: #d9d9d9;
    --accent-blue: #1a8fcf;
    --accent-orange: #f0a02b;
    --icon: #cfcfcf;
  }
  * { box-sizing: border-box; margin: 0; padding: 0; }
  html, body { width: 1200px; height: 900px; overflow: hidden; }
  body {
    background: var(--page);
    font-family: "Open Sans", Arial, sans-serif;
    display: flex;
    flex-direction: column;
    align-items: center;
    justify-content: center;
    gap: 40px;
  }
  .card {
    width: 700px;
    height: 400px;
    border-radius: 22px;
    background: radial-gradient(ellipse at 50% 40%, #303032 0%, var(--card) 60%, var(--card-edge) 100%);
    position: relative;
    overflow: hidden;
    box-shadow: 0 6px 18px rgba(0,0,0,.25);
  }

  /* back side */
  .company-block {
    position: absolute;
    left: 48px;
    bottom: 56px;
  }
  .company-name {
    font-family: "Open Sans", Arial, sans-serif;
    font-weight: 600;
    font-size: 30px;
    letter-spacing: 2px;
    text-transform: uppercase;
    color: var(--ink);
    line-height: 1.15;
  }
  .contact-block {
    position: absolute;
    left: 380px;
    top: 54px;
    color: var(--ink);
  }
  .person-name {
    font-family: "Roboto Slab", Georgia, serif;
    font-weight: 600;
    font-size: 24px;
    letter-spacing: 1px;
    text-transform: uppercase;
  }
  .person-title {
    font-size: 13px;
    font-weight: 600;
    color: var(--accent-blue);
    margin-bottom: 18px;
  }
  .contact-list { list-style: none; }
  .contact-list li {
    display: flex;
    align-items: flex-start;
    gap: 14px;
    font-size: 15px;
    line-height: 1.3;
    color: var(--ink-soft);
    margin-bottom: 9px;
  }
  .contact-list svg {
    width: 14px;
    height: 14px;
    flex: none;
    margin-top: 3px;
    fill: var(--icon);
  }

  /* front side */
  .front .brand-mark {
    position: absolute;
    inset: 0;
    display: flex;
    align-items: center;
    justify-content: center;
    gap: 16px;
  }
  .brand-dot {
    width: 22px;
    height: 22px;
    border-radius: 50%;
    background: var(--accent-orange);
  }
  .brand-name {
    font-family: "Open Sans", Arial, sans-serif;
    font-weight: 600;
    font-size: 34px;
    letter-spacing: 3px;
    text-transform: uppercase;
    color: var(--accent-blue);
  }
</style>
</head>
<body>

  <section class="card back" aria-label="Business card back">
    <div class="company-block">
      <div class="company-name">Brindle<br>Logistics, LLC</div>
    </div>

    <div class="contact-block">
      <div class="person-name">Daniel R. Moore</div>
      <div class="person-title">Founder / CEO</div>
      <ul class="contact-list">
        <li>
          <svg viewBox="0 0 16 16" aria-hidden="true"><path d="M4 1l2.5 3-1.5 2c1 2 3 4 5 5l2-1.5 3 2.5-1.5 2.5C8 15 1 8 1.5 2.5z"/></svg>
          +64 (0)9555 0142
        </li>
        <li>
          <svg viewBox="0 0 16 16" aria-hidden="true"><path d="M1 5c2-3 12-3 14 0l-1 2h-3V5H5v2H2z M3 8h10l1 6H2z"/></svg>
          021 555 018
        </li>
        <li>
          <svg viewBox="0 0 16 16" aria-hidden="true"><path d="M1 3h14v10H1z M2 4l6 5 6-5" stroke="#2a2a2c" stroke-width="1"/></svg>
          info@brindlelogistics.com
        </li>
        <li>
          <svg viewBox="0 0 16 16" aria-hidden="true"><circle cx="8" cy="8" r="7"/><path d="M1 8h14M8 1c-3 3-3 11 0 14M8 1c3 3 3 11 0 14" stroke="#2a2a2c" stroke-width="1" fill="none"/></svg>
          www.brindlelogistics.com
        </li>
        <li>
          <svg viewBox="0 0 16 16" aria-hidden="true"><path d="M8 1a5 5 0 0 1 5 5c0 4-5 9-5 9S3 10 3 6a5 5 0 0 1 5-5z"/><circle cx="8" cy="6" r="2" fill="#2a2a2c"/></svg>
          <span>14 Kestrel Lane,<br>Riverton, Auckland 1042,<br>New Zealand</span>
        </li>
      </ul>
    </div>
  </section>

  <section class="card front" aria-label="Business card front">
    <div class="brand-mark">
      <span class="brand-dot"></span>
      <span class="brand-name">Brindle Logistics</span>
    </div>
  </section>

</body>
</html>
```